The WILLOW Lodge is a transitional living housue for women in recovery. It is structured and loving an

I have uploaded my old brochure which was not designed professionally. I want a fresh, funky feel. Our website is www.willowlodgeofthebrightcoast.example if you want to get ideas from that but I do not like the bubbles on it. I have uploded a few pics of the houses and the backyards. Please help us convey love and hope and recovery!

Industry/Entity Type

House

```html
<!DOCTYPE html>
<html lang="en">
<head>
<meta charset="utf-8">
<title>The WILLOW Lodge – Tri-fold Brochure</title>
<link rel="stylesheet" href="https://fonts.googleapis.com/css2?family=Cormorant+Garamond:ital,wght@0,500;0,600;1,600&family=Lora:ital,wght@0,400;1,400&family=Josefin+Sans:wght@400&display=swap">
<style>
  :root {
    --backdrop: #e9ebe6;
    --paper: #f7f8f3;
    --photo-deck-light: #e4e6df;
    --photo-deck-mid: #c9ccc0;
    --photo-leaf: #cbd6bd;
    --photo-house-light: #eef3e4;
    --photo-house-mid: #c9d8b2;
    --photo-house-deep: #a9bf90;
    --band-lime: #e6f2c9;
    --accent-lime: #a9d45a;
    --name-ink: #4b6a25;
    --band-ink: #8cab52;
    --heading-purple: #6a4e9c;
    --body-ink: #4a4d46;
    --note-green: #6f9a3a;
    --small-ink: #6c6f68;
    --contact-veil: rgba(255,255,255,0.35);
    --fold-line: #d9dcd3;
  }
  * { box-sizing: border-box; margin: 0; padding: 0; }
  html, body { width: 1200px; height: 900px; overflow: hidden; background: var(--backdrop); }
  .brochure {
    position: absolute; left: 45px; top: 20px;
    width: 1110px; height: 860px;
    display: flex; background: var(--paper);
    box-shadow: 0 2px 10px rgba(0,0,0,0.12);
  }
  .panel { position: relative; width: 370px; height: 860px; overflow: hidden; }
  .panel + .panel { border-left: 1px solid var(--fold-line); }

  /* Inside panel: Sisters & Supports */
  .panel--sisters .photo {
    position: absolute; inset: 0;
    background:
      radial-gradient(ellipse at 25% 20%, var(--photo-leaf) 0%, transparent 55%),
      linear-gradient(160deg, var(--photo-deck-light) 0%, var(--photo-deck-mid) 60%, var(--photo-deck-light) 100%);
  }
  .panel--sisters .copy { position: relative; padding: 70px 34px 0 34px; }
  .section-heading {
    font-family: "Cormorant Garamond", serif; font-style: italic; font-weight: 600;
    font-size: 32px; color: var(--heading-purple); margin-bottom: 16px;
  }
  .body-copy {
    font-family: "Lora", serif; font-size: 17px; line-height: 1.72; color: var(--body-ink);
  }
  .location-note {
    margin-top: 70px;
    font-family: "Lora", serif; font-style: italic; font-size: 18px; line-height: 1.6;
    color: var(--note-green);
  }

  /* Middle panel */
  .panel--about { background: var(--paper); padding: 70px 36px; }
  .small-copy {
    font-family: "Lora", serif; font-size: 12.5px; line-height: 1.8; color: var(--small-ink);
    margin-bottom: 22px;
  }
  .brand-mark {
    display: flex; align-items: center; gap: 10px; justify-content: center;
    margin: 150px 0 40px;
  }
  .brand-mark .dot { width: 14px; height: 14px; border-radius: 50%; background: var(--accent-lime); }
  .brand-mark .name {
    font-family: "Cormorant Garamond", serif; font-weight: 600; font-size: 20px; color: var(--name-ink);
  }

  /* Cover panel */
  .panel--cover .photo {
    position: absolute; inset: 0;
    background:
      radial-gradient(ellipse at 70% 18%, var(--photo-house-light) 0%, transparent 45%),
      radial-gradient(ellipse at 50% 62%, var(--photo-house-deep) 0%, transparent 60%),
      linear-gradient(180deg, var(--photo-house-mid) 0%, var(--photo-house-deep) 55%, var(--photo-house-mid) 100%);
  }
  .cover-band {
    position: absolute; left: 0; top: 0; width: 100%; height: 120px;
    background: linear-gradient(180deg, var(--band-lime) 40%, rgba(230,242,201,0));
    text-align: center; padding-top: 24px;
  }
  .cover-region {
    font-family: "Josefin Sans", sans-serif; font-size: 28px; letter-spacing: 6px; color: var(--band-ink);
  }
  .cover-tagline {
    font-family: "Josefin Sans", sans-serif; font-size: 15px; letter-spacing: 2.5px; color: var(--band-ink);
    margin-top: 4px;
  }
  .cover-name {
    position: absolute; left: 0; right: 0; top: 220px;
    display: flex; align-items: center; justify-content: center; gap: 12px;
  }
  .cover-name .square { width: 16px; height: 16px; background: var(--accent-lime); }
  .cover-name .name {
    font-family: "Josefin Sans", sans-serif; font-weight: 400; font-size: 30px; color: var(--name-ink);
  }
  .contact-card {
    position: absolute; left: 24px; right: 24px; bottom: 110px;
    background: var(--contact-veil); padding: 24px 16px;
    font-family: "Lora", serif; font-style: normal; color: #fff; font-size: 12px; line-height: 2.1;
    overflow-wrap: anywhere;
  }
</style>
</head>
<body>
  <main class="brochure">
    <section class="panel panel--sisters">
      <div class="photo" role="img" aria-label="Faded photograph of a wooden backyard deck and garden greenery"></div>
      <div class="copy">
        <h2 class="section-heading">Sisters &amp; Supports</h2>
        <p class="body-copy">The WILLOW Lodge is known for its loving and instant support system for women in early recovery. We offer a safe and structured place to live with sisters who share their goals. It is a home with a lower rent designed for women to save money. We practice the principles of recovery and offer beautiful homes for women to live and visit. No one ever has to be alone during early recovery.</p>
        <p class="location-note">We are located close to Bright Coast beaches, parks, churches, shopping and schools.</p>
      </div>
    </section>

    <section class="panel panel--about">
      <p class="small-copy">Our homes offer a calm, structured place to rebuild daily life. Each resident shares chores, attends meetings and keeps a steady routine with the help of house staff.</p>
      <p class="small-copy">Residents are encouraged to work, study or volunteer while saving money for the next step. Weekly house meetings keep everyone connected and accountable.</p>
      <div class="brand-mark">
        <span class="dot"></span>
        <span class="name">The WILLOW Lodge</span>
      </div>
      <p class="small-copy">Call or visit today to learn about availability, fees and what to expect on your first day with us.</p>
    </section>

    <section class="panel panel--cover">
      <div class="photo" role="img" aria-label="Soft photograph of a small house with a red door, window and white picket fence under trees"></div>
      <header class="cover-band">
        <p class="cover-region">Bright Coast</p>
        <p class="cover-tagline">Recovery Homes for Women</p>
      </header>
      <div class="cover-name">
        <span class="square"></span>
        <h1 class="name">The WILLOW Lodge</h1>
      </div>
      <address class="contact-card">
        Seaview, FL<br>
        (555) 014-2280<br>
        www.willowlodgeofthebrightcoast.example<br>
        hello@willowlodgeofthebrightcoast.example
      </address>
    </section>
  </main>
</body>
</html>
```